Business Card & Stationary Design Project

We are looking for some creative direction for business cards and our stationary.

We are a global logistics firm that has recently changed its name to Marrick Global Logistics and we have a new website due out tomorrow (www.marrick.com.au).

The colours of the company are rich navy tones, I would like to have business cards that fit together to make one picture on the back (possibly an old map of the world??), and the front to be modern contemporary looking.

But I am open to suggestions, so just incorporate our new logo and get going!
Updates

Hi Everyone,

Thank you for all of your designs so far and the time you have put into it.

I have asked many of you for amendments to see if we can get a final product, so with this in mind I am extending the deadline by a few days.

Good luck and thank you once again.

Please message me direct if you need any clarification.

Kind Regards
Colin

Reason: As outlined the extra 3 days is for amendments and changes to the current submissions. Thanks Colin

Industry/Entity Type

Business

```html
<!DOCTYPE html>
<html lang="en">
<head>
<meta charset="utf-8">
<title>Marrick Global Logistics – Business Card</title>
<link rel="stylesheet" href="https://fonts.googleapis.com/css2?family=Open+Sans:wght@400&display=swap">
<style>
  :root {
    --band-dark: #2a2d3c;
    --panel-white: #ffffff;
    --brand-navy: #0d1566;
    --contact-text: #ffffff;
    --art-light: #4d9fe0;
    --art-deep: #14519e;
  }
  html, body {
    margin: 0;
    padding: 0;
    width: 1200px;
    height: 848px;
    overflow: hidden;
    background: var(--band-dark);
  }
  .card {
    position: relative;
    width: 1200px;
    height: 848px;
    background: var(--band-dark);
    font-family: "Open Sans", Arial, sans-serif;
  }
  .brand-panel {
    position: absolute;
    left: 0;
    top: 175px;
    width: 1200px;
    height: 341px;
    background: var(--panel-white);
  }
  .wordmark-name,
  .wordmark-tagline {
    position: absolute;
    left: 175px;
    margin: 0;
    color: var(--brand-navy);
    font-family: "Open Sans", Arial, sans-serif;
    font-weight: 400;
    text-transform: uppercase;
    line-height: 1;
    white-space: nowrap;
  }
  .wordmark-name {
    top: 272px;
    font-size: 56px;
    letter-spacing: 0.94em;
  }
  .wordmark-tagline {
    top: 342px;
    font-size: 24px;
    letter-spacing: 0.95em;
  }
  .globe-art {
    position: absolute;
    left: 774px;
    top: 185px;
    width: 252px;
    height: 252px;
    background: linear-gradient(160deg, var(--art-light), var(--art-deep));
  }
  .contact-list {
    position: absolute;
    left: 81px;
    top: 525px;
    margin: 0;
    padding: 0;
    list-style: none;
    color: var(--contact-text);
    font-size: 38px;
    line-height: 51px;
    font-weight: 400;
    white-space: nowrap;
  }
</style>
</head>
<body>
  <div class="card">
    <div class="brand-panel"></div>

    <p class="wordmark-name">Marrick</p>
    <p class="wordmark-tagline">Global Logistics</p>

    <div class="globe-art" role="img" aria-label="Illustration of a glossy blue globe showing Asia and Australia"></div>

    <ul class="contact-list">
      <li>Address: 217 Wharf Road Millers Point NSW 2000</li>
      <li>Phone: 02 9471 2260</li>
      <li>Mobile: 0412583619</li>
      <li>Fax: 029471 2261</li>
      <li>Email: colin@marrick.com.au</li>
      <li>Web: marrick.com.au</li>
    </ul>
  </div>
</body>
</html>
```